Coralvale Jukebox and Jumping Castle Hire

Hi folks,
This is for a new business based in Coralvale(Australia), the business hires, jukeboxes, inflatable games(mostly jumping castles) and slushy/cocktail machines.
I want the website to appeal to people looking to party. Does that sound too simplistic?
It should be simple to navigate, I require only the front page but make it easy to get to the rest of the site.
Modern, exciting and funky, think rock band or concert promoter.
We are trying to sell packages of products, there should be several packages visible on the front page without looking cluttered.
Link to jukebox song list.
Friendlane, pondlet etc.
I am currently on holidays so I have a fair amount of time to get this project done, it says 10 days I hope to have it done much sooner.

Reason: So far there is no design that I am happy with. I am after a website for Jukeboxes, it should have a rock concert feel.

Ages 20 to 50

Business

• Think rock band type website, black with bold color highlight.
• Plain or bland color.
Pictures of Coralvale or any other city.
Vexaro map or any other location type map.

```html
<!DOCTYPE html>
<html lang="en">
<head>
<meta charset="utf-8">
<title>Coralvale Jukebox and Jumping Castle Hire</title>
<link rel="stylesheet" href="https://fonts.googleapis.com/css2?family=Open+Sans:wght@400;600;700;800&family=PT+Serif&display=swap">
<style>
:root{
  --black:#000;
  --white:#fff;
  --orange:#ffa200;
  --orange-deep:#ff8a00;
  --orange-light:#ffbf1a;
  --grey-field:#dcdcdc;
  --grey-icon:#5a5a5a;
  --grey-arrow:#3a3a3a;
  --line:#cfcfcf;
  --sans:"Open Sans",sans-serif;
  --serif:"PT Serif",serif;
}
*{margin:0;padding:0;box-sizing:border-box}
html,body{width:821px;height:1200px;overflow:hidden;background:var(--black)}
.page{position:relative;width:821px;height:1200px;background:var(--black);font-family:var(--sans);color:var(--white)}
.abs{position:absolute}

/* hero */
.hero{left:0;top:0;width:821px;height:424px;
  background:radial-gradient(ellipse at 50% 35%,#c98a63 0%,#7a4a33 22%,#3a2a26 45%,#1d2a22 70%,#0c120e 100%)}
.brand{left:88px;top:0;width:116px;height:100px;background:var(--black);text-align:center;padding-top:52px;color:var(--white);font-weight:600}
.brand-name{font-size:19px;line-height:20px;letter-spacing:1px}
.brand-sub{font-size:7px;line-height:10px}
.brand-dot{display:block;width:26px;height:26px;border-radius:50%;background:var(--orange);position:absolute;left:45px;top:16px}
.social-top{left:663px;top:13px;display:flex;gap:3px}
.social-top span{width:12px;height:12px;border-radius:50%;background:var(--white)}
.nav{left:259px;top:41px;width:473px;height:36px;background:rgba(0,0,0,.85);border-radius:3px}
.nav ul{list-style:none;display:flex;position:absolute;left:33px;top:10px}
.nav li{font-size:10px;padding:2px 11px;border-radius:3px;line-height:14px}
.nav li.active{background:var(--orange);padding:2px 12px}
.search{left:337px;top:9px;width:126px;height:18px;background:#e6e6e6;border-radius:2px;font-size:9px;color:#aaa;font-style:italic;padding:3px 12px}
.arrow{width:30px;height:30px;top:220px}
.arrow-prev{left:89px}
.arrow-next{left:701px}
.caption{left:237px;top:328px;width:346px;height:39px;background:rgba(0,0,0,.75);font-weight:800;font-size:21px;text-align:center;line-height:39px;letter-spacing:-.3px}

/* welcome band */
.welcome{left:0;top:424px;width:821px;height:93px;background:linear-gradient(var(--orange-light),var(--orange-deep));color:var(--black);text-align:center}
.welcome h1{font-size:19px;font-weight:700;margin-top:23px;line-height:24px}
.welcome h2{font-size:26px;font-weight:400;line-height:32px}

/* intro */
.intro{left:120px;top:537px;width:581px;font-size:7.6px;line-height:11px;text-align:center}
.btn{background:var(--orange);color:var(--black);font-family:var(--serif);font-size:6.5px;text-transform:uppercase;text-align:center;border:1px solid #ffcc55;line-height:16px;height:18px}
.btn-intro{left:386px;top:572px;width:49px}

/* packages */
.photo{position:absolute}
.ph-jukebox{left:88px;top:617px;width:217px;height:154px;background:linear-gradient(120deg,#0a1a5a,#3a3fa0 45%,#8a5a4a 75%,#2a2a3a)}
.ph-cocktail{left:516px;top:617px;width:218px;height:154px;background:linear-gradient(110deg,#1a0a14,#c8306a 30%,#9ad021 55%,#7a3aa8 80%,#140a18)}
.ph-castle{left:305px;top:771px;width:211px;height:155px;background:linear-gradient(170deg,#2a6a2a,#2a3ad0 35%,#e0e020 55%,#c83030 75%,#5a6a7a)}
.pkg h3{font-size:14px;font-weight:400;color:var(--orange);letter-spacing:.5px;text-transform:uppercase;line-height:18px}
.pkg p{font-size:9px;line-height:11.5px;margin-top:10px}
.pkg-inflatable{left:320px;top:635px;width:188px}
.pkg-jukebox{left:97px;top:794px;width:200px}
.pkg-slushy{left:530px;top:794px;width:204px}
.btn-inflatable{left:453px;top:733px;width:48px}
.btn-jukebox{left:246px;top:904px;width:48px}
.btn-slushy{left:685px;top:904px;width:48px}

/* footer */
.footer-line{left:0;top:959px;width:821px;height:3px;background:var(--orange)}
.footer-tab{left:396px;top:945px}
.f-head{font-size:12px;color:var(--orange);text-transform:uppercase;letter-spacing:.3px}
.fh-social{left:87px;top:973px}
.fh-adv{left:308px;top:973px}
.fh-contact{left:551px;top:973px}
.f-icons{left:87px;top:997px;display:flex;gap:9px}
.f-icons span{width:25px;height:25px;border-radius:50%;background:var(--grey-icon)}
.f-icons span.on{background:var(--orange)}
.blogs{left:87px;top:1048px;width:175px}
.blogs h4{font-size:12px;font-weight:400;text-transform:uppercase}
.post-title{font-size:8.5px;margin-top:8px}
.post-date{font-size:6px;color:var(--orange);margin-top:4px}
.post-body{font-size:7.8px;line-height:11px;margin-top:3px}
.read-more{font-family:var(--serif);font-size:7.5px;color:var(--orange);margin-top:8px}
.adv-list{left:308px;top:996px;width:180px;list-style:none}
.adv-list li{font-size:6.6px;height:17px;line-height:14px;border-bottom:1px solid var(--line);padding-left:2px}
.adv-list li::before{content:"»";margin-right:5px;color:#aaa}
.field{left:551px;width:180px;background:var(--grey-field);font-family:var(--serif);font-size:7.5px;color:#888;padding:4px 6px}
.f-name{top:996px;height:20px}
.f-email{top:1021px;height:20px}
.f-msg{top:1045px;height:77px}
.btn-submit{left:685px;top:1140px;width:48px;height:19px;font-family:var(--sans);font-size:7.5px;line-height:17px}
.bottom-bar{left:0;top:1181px;width:821px;height:19px;background:linear-gradient(var(--orange-light),var(--orange-deep))}
</style>
</head>
<body>
<div class="page">

  <header>
    <div class="abs hero" role="img" aria-label="Hero photo: a woman with headphones dancing at a DJ deck in a club"></div>
    <div class="abs brand">
      <span class="brand-dot"></span>
      <div class="brand-name">CORALVALE</div>
      <div class="brand-sub">Jukebox and Jumping Castle Hire</div>
    </div>
    <div class="abs social-top" aria-label="Social links">
      <span aria-label="Linkora"></span><span aria-label="Friendlane"></span><span aria-label="Vexaro"></span><span aria-label="pondlet"></span><span aria-label="Vidstream"></span>
    </div>
    <nav class="abs nav">
      <ul>
        <li class="active">Home</li><li>About</li><li>FAQ</li><li>Order</li><li>Contact</li>
      </ul>
      <div class="abs search">Search</div>
    </nav>
    <svg class="abs arrow arrow-prev" viewBox="0 0 30 30" aria-label="Previous slide"><circle cx="15" cy="15" r="15" fill="#ffa200"/><path d="M18 8 L11 15 L18 22" stroke="#3a2a00" stroke-width="3" fill="none"/></svg>
    <svg class="abs arrow arrow-next" viewBox="0 0 30 30" aria-label="Next slide"><circle cx="15" cy="15" r="15" fill="#3a3a3a"/><path d="M12 8 L19 15 L12 22" stroke="#0a0a0a" stroke-width="3" fill="none"/></svg>
    <div class="abs caption">JokeBox &amp; Jumping Castle</div>
  </header>

  <section class="abs welcome">
    <h1>Welcome To Coralvale</h1>
    <h2>Jukebox &amp; Jumping Castle Hire</h2>
  </section>

  <p class="abs intro">Contrary to popular belief, Lorem Ipsum is not simply random text. It has roots in a piece of classical Latin literature from 45 BC, making it over 2000 years old. Harold Penwick, a Latin professor at Ashford-Vale College in Vermont, looked up one of the more obscure Latin words, consectetur</p>
  <div class="abs btn btn-intro">Learn More</div>

  <section class="packages">
    <div class="photo ph-jukebox" role="img" aria-label="Photo of a smiling man beside a touchscreen jukebox"></div>
    <div class="photo ph-cocktail" role="img" aria-label="Photo of colourful slushy cocktails in glasses"></div>
    <div class="photo ph-castle" role="img" aria-label="Photo of an inflatable jumping castle"></div>

    <div class="abs pkg pkg-inflatable">
      <h3>Inflatable Games</h3>
      <p>Phasellus porta. Fusce suscipit varius mi. Cum sociis natoque penatibus et magnis dis parturient montes, Phasellus porta. Fusce suscipit varius mi. Cum sociis natoque penatibus et magnis dis parturient montes,</p>
    </div>
    <div class="abs btn btn-inflatable">Learn More</div>

    <div class="abs pkg pkg-jukebox">
      <h3>Jukeboxes</h3>
      <p>Phasellus porta. Fusce suscipit varius mi. Cum sociis natoque penatibus et magnis dis parturient montes, Phasellus porta. Fusce suscipit varius mi. Cum sociis natoque penatibus et magnis dis parturient montes,</p>
    </div>
    <div class="abs btn btn-jukebox">Learn More</div>

    <div class="abs pkg pkg-slushy">
      <h3>Slushy / Cocktail</h3>
      <p>Phasellus porta. Fusce suscipit varius mi. Cum sociis natoque penatibus et magnis dis parturient montes, Phasellus porta. Fusce suscipit varius mi. Cum sociis natoque penatibus et magnis dis parturient montes,</p>
    </div>
    <div class="abs btn btn-slushy">Learn More</div>
  </section>

  <footer>
    <svg class="abs footer-tab" width="28" height="16" viewBox="0 0 28 16" aria-hidden="true"><path d="M0 16 L14 1 L28 16 Z" fill="#ffa200"/><rect x="10" y="9" width="8" height="1.6" fill="#000"/></svg>
    <div class="abs footer-line"></div>

    <div class="abs f-head fh-social">Social Links</div>
    <div class="abs f-icons">
      <span class="on" aria-label="Friendlane"></span><span aria-label="pondlet"></span><span aria-label="Linkora"></span>
    </div>
    <div class="abs blogs">
      <h4>Blogs</h4>
      <div class="post-title">Post Title</div>
      <div class="post-date">Friday, 6th April 2000</div>
      <p class="post-body">Lorem ipsum dolor sit amet, consectetur adipiscing elit. Nunc non diam erat. In fringilla massa ut nisi ullamcorper pellentesque.</p>
      <div class="read-more">Read More »</div>
    </div>

    <div class="abs f-head fh-adv">Advertise With Us</div>
    <ul class="abs adv-list">
      <li>Lorem ipsum dolor sit</li><li>Amet consectetur</li><li>Praesent vel sem id</li><li>Curabitur hendrerit est</li><li>Aliquam eget erat nec sapien</li><li>Cras id augue nunc</li><li>In nec justo non</li><li>Vivamus mollis enim ut</li><li>Curabitur hendrerit est</li>
    </ul>

    <div class="abs f-head fh-contact">Contact Us</div>
    <div class="abs field f-name">Name</div>
    <div class="abs field f-email">Email</div>
    <div class="abs field f-msg">Massages</div>
    <div class="abs btn btn-submit">SUBMIT</div>

    <div class="abs bottom-bar"></div>
  </footer>
</div>
</body>
</html>
```